Criação de Folder para Rocha & Brisa
" Trabalhamos com locação de usinas de energia fotovoltaica! Nosso cliente não precisa investir nada para instalação e nem manutenção do sistema por todo o período de 25 anos. Garantimos a economia e pleno funcionamento por todo o período. O cliente tem uma redução de até 50% na conta de luz (desconto progressivo). Já investimos mais de 2 milhões em projetos de energia renovável em todo o Brasil. Operamos no mercado de energia renovável desde 2016, são mais de 733 unidades consumidoras atendidas e todos os projetos sempre foram zero investimento por parte dos clientes. "

```html
<!DOCTYPE html>
<html lang="pt-BR">
<head>
<meta charset="UTF-8">
<title>Folder Rocha &amp; Brisa</title>
<link href="https://fonts.googleapis.com/css2?family=Montserrat:wght@700;800&family=Open+Sans:wght@400;600&display=swap" rel="stylesheet">
<style>
  :root {
    --navy: #1b2f52;
    --blue: #1a6fb8;
    --blue-dark: #0d4786;
    --sun: #f2b31b;
    --text: #5a5f66;
    --paper: #ffffff;
    --backdrop: #e6e8eb;
    --photo-a: #9fc3df;
    --photo-b: #4f86b3;
  }
  * { box-sizing: border-box; margin: 0; padding: 0; }
  html, body { width: 1200px; height: 1200px; overflow: hidden; }
  body {
    background: var(--backdrop);
    font-family: "Open Sans", sans-serif;
    color: var(--text);
    display: flex; align-items: center; justify-content: center;
  }
  .folder-page {
    width: 1120px; height: 1130px;
    background: var(--paper);
    box-shadow: 0 6px 24px rgba(0,0,0,.12);
    display: flex;
    padding: 60px 0 50px 70px;
    overflow: hidden;
  }
  .content { width: 790px; flex: none; }
  .aside {
    flex: 1; padding-left: 36px;
    display: flex; flex-direction: column;
  }
  .section-title {
    font-family: "Montserrat", sans-serif;
    font-weight: 800; font-size: 28px;
    color: var(--navy); letter-spacing: .5px;
    display: inline-block;
    border-bottom: 4px solid var(--sun);
    padding-bottom: 4px; margin-bottom: 16px;
  }
  .about p {
    font-size: 19px; line-height: 1.5;
    text-align: justify; margin-bottom: 16px;
  }
  .benefits { margin-top: 20px; }
  .benefit {
    display: flex; align-items: flex-start; gap: 24px;
    margin: 14px 0 22px;
  }
  .benefit-icon {
    flex: none; width: 84px; height: 84px; border-radius: 14px;
    background: linear-gradient(145deg, var(--blue), var(--blue-dark));
    display: flex; align-items: center; justify-content: center;
  }
  .benefit-icon svg { width: 52px; height: 52px; }
  .benefit h3 {
    font-family: "Montserrat", sans-serif;
    font-weight: 700; font-size: 25px; color: var(--navy);
    margin-bottom: 2px;
  }
  .benefit p { font-size: 19px; line-height: 1.4; }
  .next-title { margin-top: 4px; margin-bottom: 0; }
  .brand {
    display: flex; align-items: center; gap: 10px;
    margin-top: 310px;
  }
  .brand-dot {
    width: 40px; height: 40px; border-radius: 50%;
    background: var(--sun); flex: none;
  }
  .brand-name {
    font-family: "Montserrat", sans-serif; font-weight: 800;
    font-size: 19px; color: var(--blue-dark); white-space: nowrap;
  }
  .aside-photo {
    margin-top: 28px; height: 540px; border-radius: 8px 0 0 8px;
    background: linear-gradient(180deg, var(--photo-a), var(--photo-b));
  }
</style>
</head>
<body>
  <main class="folder-page">
    <div class="content">
      <section class="about">
        <h2 class="section-title">QUEM SOMOS</h2>
        <p>Startup criada, equipe preparada, começamos com tudo no mercado de energia, 1ª empresa a fazer usinas compartilhadas em SC, além de aparecer no Arena Empreende.</p>
        <p>Operamos desde 2016 no mercado de energia e já atendemos mais de 744 unidades consumidoras, fomos finalistas do Energia Starter Lab em SP e vencedores do Impulso Criativo no CE em 2017, startup premiada, implementamos serviços inovadores na área de energia renovável para Cidade Viva Laguna.</p>
        <p>Em 2019 houve a inauguração de nossa 1ª usina de biogas em SC, e começamos a atender os condomínios da grande Florianópolis, desenvolvimento de serviço focados nas necessidades dos condomínios.</p>
      </section>

      <section class="benefits">
        <h2 class="section-title">NOSSOS BENEFÍCIOS</h2>

        <div class="benefit">
          <div class="benefit-icon">
            <svg viewBox="0 0 58 58" fill="none" stroke="#fff" stroke-width="4" stroke-linecap="round" stroke-linejoin="round">
              <rect x="8" y="6" width="42" height="46" rx="4"/>
              <path d="M20 42V20M14 26l6-6 6 6M36 42V16M30 22l6-6 6 6"/>
            </svg>
          </div>
          <div>
            <h3>Economia na Conta de Energia</h3>
            <p>reduza de forma efetiva a sua conta de energia, pelos próximos 25 anos.</p>
          </div>
        </div>

        <div class="benefit">
          <div class="benefit-icon">
            <svg viewBox="0 0 58 58" fill="none" stroke="#fff" stroke-width="4" stroke-linecap="round" stroke-linejoin="round">
              <path d="M12 46l22-22M36 12a8 8 0 1 0 10 10l-6-1-3-3z"/>
              <path d="M12 12l30 30M10 10l4-2 4 4-2 4z"/>
            </svg>
          </div>
          <div>
            <h3>Manutenção</h3>
            <p>Precisou trocar, limpar, arrumar ou atualizar, nosso time entra em cena e faz todo trabalho, sem custo.</p>
          </div>
        </div>

        <div class="benefit">
          <div class="benefit-icon">
            <svg viewBox="0 0 58 58" fill="none" stroke="#fff" stroke-width="4" stroke-linecap="round" stroke-linejoin="round">
              <rect x="5" y="16" width="48" height="26" rx="3"/>
              <circle cx="29" cy="29" r="6"/>
              <path d="M12 29h2M44 29h2"/>
            </svg>
          </div>
          <div>
            <h3>Zero investimento</h3>
            <p>Neste momento estamos realizando locação de usinas sem contra partida, ou seja zero de investimento.</p>
          </div>
        </div>

        <div class="benefit">
          <div class="benefit-icon">
            <svg viewBox="0 0 58 58" fill="none" stroke="#fff" stroke-width="4" stroke-linecap="round" stroke-linejoin="round">
              <path d="M12 6h24l10 10v36H12z"/>
              <path d="M36 6v10h10"/>
              <path d="M34 26h-7a4 4 0 0 0 0 8h4a4 4 0 0 1 0 8h-7M29 22v4M29 42v4"/>
            </svg>
          </div>
          <div>
            <h3>Possibilidade de compra</h3>
            <p>Depois de instalarmos, gostou e quer mais economia? Pode consultar nosso plano de aquisição da usina.</p>
          </div>
        </div>

        <h2 class="section-title next-title">POR QUE NOS ESCOLHEMOS?</h2>
      </section>
    </div>

    <aside class="aside">
      <div class="brand">
        <span class="brand-dot"></span>
        <span class="brand-name">Rocha &amp; Brisa</span>
      </div>
      <div class="aside-photo" role="img" aria-label="Foto de usina solar com painéis fotovoltaicos"></div>
    </aside>
  </main>
</body>
</html>
```